Need Business Cards for my Business

email address: rkpmarlowhollowworks@vendrimail.com
web address: rkpmarlowhollowworks.net
Slogan: We offer various QVN licenses
Rowland K. Pemberly
Please stick with colors of Company Logo
would like the card to be more of the color example of the logo.
If you need PDF copy of logo email me at the above account.
Creative control rests with you.

Industry/Entity Type

Business

Contact Information for Business Card

I am a minimalist, but would like something to pop and stand out amongst other cards, make it memorable.

Font styles to use
Serif
Decorative
Script

```html
<!DOCTYPE html>
<html lang="en">
<head>
<meta charset="utf-8">
<title>Marlow Hollow Aeronautics – Business Cards</title>
<link href="https://fonts.googleapis.com/css2?family=Open+Sans:ital,wght@0,400;0,800;1,700&display=swap" rel="stylesheet">
<style>
  :root {
    --backdrop: #e9e6e2;
    --card-white: #ffffff;
    --navy: #1d4a7f;
    --navy-deep: #163b68;
    --accent-red: #e3262f;
    --back-blue: #2c7fc3;
    --back-blue-soft: #2a78b9;
    --ink-white: #ffffff;
  }
  html, body {
    margin: 0;
    width: 1200px;
    height: 900px;
    overflow: hidden;
    background: var(--backdrop);
    font-family: "Open Sans", Arial, sans-serif;
  }
  .canvas { position: relative; width: 1200px; height: 900px; }

  .card { position: absolute; overflow: hidden; box-shadow: 0 3px 10px rgba(0,0,0,.18); }

  .wordmark {
    display: flex; align-items: center; gap: 14px;
    font-weight: 800; font-size: 24px; letter-spacing: .3px; line-height: 1;
    text-transform: uppercase; white-space: nowrap;
  }
  .wordmark-dot { width: 24px; height: 24px; border-radius: 50%; flex: none; }

  /* Front */
  .card-front { left: 78px; top: 34px; width: 588px; height: 363px; background: var(--card-white); }
  .front-bands { position: absolute; left: 0; top: 0; width: 588px; height: 363px; }
  .card-front .wordmark {
    position: absolute; left: 62px; top: 94px;
    color: var(--navy);
  }
  .card-front .wordmark-dot { background: var(--navy); }
  .holder-name {
    position: absolute; left: 55px; top: 234px; margin: 0;
    color: var(--ink-white); font-weight: 700; font-style: italic; font-size: 24px;
    line-height: 1.2; text-transform: uppercase; letter-spacing: -.2px;
  }
  .contact-list { position: absolute; left: 55px; top: 277px; margin: 0; padding: 0; list-style: none; }
  .contact-list li {
    display: flex; align-items: center; gap: 8px; height: 21.5px;
    color: var(--ink-white); font-size: 15px;
  }
  .contact-list svg { width: 12px; height: 12px; flex: none; }

  /* Back */
  .card-back { left: 389px; top: 505px; width: 566px; height: 352px; background: var(--back-blue); }
  .back-pattern {
    position: absolute; inset: 0;
    background: linear-gradient(135deg, var(--back-blue) 0%, var(--back-blue-soft) 100%);
  }
  .card-back .wordmark {
    position: absolute; left: 0; right: 0; top: 164px;
    justify-content: center;
    color: var(--ink-white);
  }
  .card-back .wordmark-dot { background: var(--ink-white); }
  .slogan {
    position: absolute; left: 0; right: 0; top: 274px; margin: 0; text-align: center;
    color: var(--ink-white); font-weight: 700; font-style: italic; font-size: 14px;
    text-transform: uppercase;
  }
</style>
</head>
<body>
<main class="canvas">

  <section class="card card-front" aria-label="Business card front">
    <svg class="front-bands" viewBox="0 0 588 363" aria-hidden="true">
      <defs>
        <linearGradient id="navyFade" x1="0" y1="0" x2="0" y2="1">
          <stop offset="0" stop-color="#163b68"/>
          <stop offset="1" stop-color="#1f5797"/>
        </linearGradient>
      </defs>
      <polygon points="0,192 390,192 366,216 0,216" fill="var(--accent-red)"/>
      <polygon points="0,218 368,218 402,181 588,181 588,363 0,363" fill="url(#navyFade)"/>
    </svg>

    <div class="wordmark"><span class="wordmark-dot"></span>Marlow Hollow Aeronautics</div>

    <h1 class="holder-name">Rowland K. Pemberly</h1>
    <ul class="contact-list">
      <li>
        <svg viewBox="0 0 12 12"><path d="M1 4c0-2 2-3 5-3s5 1 5 3l-2 1-1-1H4L3 5zM3 6h6l1 5H2z" fill="#fff"/></svg>
        410-555-0183
      </li>
      <li>
        <svg viewBox="0 0 12 12"><rect x="1" y="2.5" width="10" height="7" fill="#fff"/><path d="M1 2.5l5 4 5-4" fill="none" stroke="#1d4a7f" stroke-width="1"/></svg>
        rkpmarlowhollowworks@vendrimail.com
      </li>
      <li>
        <svg viewBox="0 0 12 12"><circle cx="6" cy="6" r="5.5" fill="#fff"/><path d="M3 4l2 1 0 2 2 1-1 2M7 2l1 2 2 0" fill="none" stroke="#1d4a7f" stroke-width="1"/></svg>
        rkpmarlowhollowworks.net
      </li>
    </ul>
  </section>

  <section class="card card-back" aria-label="Business card back">
    <div class="back-pattern" role="img" aria-label="Repeating brand-mark pattern in soft blue tones"></div>
    <div class="wordmark"><span class="wordmark-dot"></span>Marlow Hollow Aeronautics</div>
    <p class="slogan">We offer various QVN licenses</p>
  </section>

</main>
</body>
</html>
```